**** Web design project for BoltNet ****

For my ICT company BoltNet I need a website.

We design, build and host web-applications and we have our own CMS product. In the references part we want to show sample websites (thumbnails) + links.

It should look modern (WEB 2.0), rounded corners.

I want the following menu' s:
- Home
- Services
- References
- News
- About BoltNet
- Contact

Sample websites:
See attachments
http://www.vandoqa.com
http://www.greyfoxmanagement.nl

Reason: Want to take some time for feedback and improvements.

Reason: I'm waiting for a black background, with shadow and ambient light. You'll make a good chance!

Industry/Entity Type

It Company

Requirements
Must have
• - Fixed width (1024px), should fit on an IPad2
- Language selection English/Dutch
- Twitter/Facebook/LinkedIn/RSS icons
- Footer for Terms of use and Copyrights
- Search box
- 3 (or more) boxes for information i.e. news, blog or advertisements
Nice to have
• - Footer Site Map
- Contrasting background outside borders
- wide image (rotator) (with transperant sentence block)
- Shadow

```html
<!DOCTYPE html>
<html lang="en">
<head>
<meta charset="utf-8">
<title>BoltNet – Web Applications</title>
<link rel="stylesheet" href="https://fonts.googleapis.com/css2?family=Titillium+Web:wght@400;600;700&display=swap">
<style>
  :root {
    --page-bg: #f6f8fb;
    --brand-blue: #2a64a0;
    --nav-top: #3d80c4;
    --nav-bottom: #1d5896;
    --nav-active: #1a4f88;
    --hero-top: #2c5d92;
    --hero-bottom: #1b3d6b;
    --hero-text: #ffffff;
    --news-top: #e6e9ed;
    --news-bottom: #c7ccd2;
    --ink-dark: #454a50;
    --ink-body: #5f6469;
    --link-blue: #1f5f9e;
    --line: #c9ced4;
    --panel: #ffffff;
    --refs-bg: #f1f2f4;
    --logo-ink: #4d7c93;
  }
  html, body {
    margin: 0;
    width: 1200px;
    height: 1034px;
    overflow: hidden;
    background: var(--page-bg);
    font-family: "Titillium Web", "Trebuchet MS", sans-serif;
  }
  .stage {
    position: relative;
    width: 1160px;
    height: 1000px;
    transform: scale(1.0345);
    transform-origin: 0 0;
    overflow: hidden;
  }
  .abs { position: absolute; }

  .top-band { left: 91px; top: 0; width: 978px; height: 6px; background: var(--brand-blue); }

  .brand { left: 92px; top: 22px; display: flex; align-items: center; gap: 14px; }
  .brand-dot { width: 64px; height: 64px; border-radius: 50%; background: var(--brand-blue); }
  .brand-name { font-size: 46px; font-weight: 400; color: var(--logo-ink); letter-spacing: 1px; line-height: 1; }

  .language { left: 899px; top: 48px; display: flex; align-items: center; gap: 8px; font-family: Arial, sans-serif; font-size: 9.5px; color: #444; }
  .language svg { display: block; }

  .main-nav {
    left: 91px; top: 110px; width: 978px; height: 50px;
    background: linear-gradient(var(--nav-top), var(--nav-bottom));
    border-radius: 6px 6px 0 0;
    display: flex;
  }
  .main-nav a {
    display: flex; align-items: center; justify-content: center;
    color: #fff; text-decoration: none; font-size: 15px;
    border-right: 1px solid rgba(10,40,80,0.45);
    box-shadow: inset -1px 0 0 rgba(255,255,255,0.12);
  }
  .main-nav a.active { background: var(--nav-active); border-radius: 6px 0 0 0; }
  .search { right: 20px; top: 12px; display: flex; gap: 6px; }
  .search input {
    width: 127px; height: 23px; box-sizing: border-box; border: 1px solid #9fb5cc; border-radius: 2px;
    font-family: Arial, sans-serif; font-size: 10px; color: #999; padding: 0 8px; background: #fff;
  }
  .search button {
    width: 52px; height: 25px; border: 1px solid #1e5fa8; border-radius: 2px;
    background: linear-gradient(#4b9ae6, #2a72c6); color: #fff; font-family: Arial, sans-serif; font-size: 10px;
  }

  .hero {
    left: 91px; top: 160px; width: 978px; height: 319px;
    background: linear-gradient(160deg, var(--hero-top), var(--hero-bottom));
    border-radius: 0 0 4px 4px;
    overflow: hidden;
  }
  .hero-title { left: 54px; top: 16px; margin: 0; font-size: 22px; font-weight: 600; color: var(--hero-text); }
  .hero-copy { left: 54px; top: 54px; width: 436px; margin: 0; font-size: 14.3px; line-height: 20px; color: #e8eef6; }
  .hero-cta {
    left: 54px; top: 222px; width: 210px; height: 68px; border-radius: 4px;
    background: linear-gradient(#3b86cc, #1d5a9a); box-shadow: 0 2px 4px rgba(0,0,0,0.35);
    color: #fff; font-size: 26px; font-weight: 700; display: flex; align-items: center; justify-content: center;
  }
  .hero-photo {
    left: 510px; top: 0; width: 468px; height: 319px;
    background: radial-gradient(ellipse at 50% 45%, #6b8fb8 0%, #2b4d78 45%, #14263f 100%);
  }
  .slider-arrow {
    top: 298px; width: 58px; height: 42px;
    background: linear-gradient(#b8cadb, #9fb5cb); border: 1px solid #8fa6bd;
    box-sizing: border-box; display: flex; align-items: center; justify-content: center;
  }

  .news-strip {
    left: 91px; top: 479px; width: 978px; height: 111px;
    background: linear-gradient(var(--news-top), var(--news-bottom));
    display: flex;
  }
  .news-item { padding: 13px 20px 0; box-sizing: border-box; border-right: 1px solid #b3b9c0; box-shadow: 1px 0 0 #eef0f2; }
  .news-item:last-child { border-right: 0; box-shadow: none; }
  .news-item h3 { margin: 0; font-size: 15px; font-weight: 600; color: var(--ink-dark); line-height: 20px; }
  .news-item p { margin: 0; font-size: 12.5px; line-height: 17px; color: #555; }
  .news-item a { font-size: 12.5px; font-weight: 600; color: var(--link-blue); text-decoration: none; line-height: 20px; }

  .why-bar {
    left: 91px; top: 590px; width: 978px; height: 48px; box-sizing: border-box;
    background: linear-gradient(#fafafa, #e4e6e8); border: 1px solid var(--line); border-radius: 5px 5px 0 0;
    box-shadow: 0 2px 3px rgba(0,0,0,0.12);
  }
  .why-bar h2 { position: absolute; left: 18px; top: 11px; margin: 0; font-size: 18.5px; font-weight: 600; color: #555; }
  .why-button {
    position: absolute; right: 18px; top: 9px; width: 100px; height: 28px; box-sizing: border-box;
    border: 1px solid #b9bdc2; border-radius: 2px; background: linear-gradient(#fff, #e9ebed);
    font-size: 12.5px; color: #444; display: flex; align-items: center; justify-content: center;
  }

  .features {
    left: 91px; top: 638px; width: 978px; height: 192px; box-sizing: border-box;
    background: var(--panel); border: 1px solid var(--line); border-top: 0;
  }
  .feature { position: absolute; width: 292px; }
  .feature h3 { margin: 0 0 14px 43px; font-size: 19px; font-weight: 600; color: var(--ink-dark); line-height: 24px; }
  .feature p { margin: 0 0 0 44px; width: 246px; font-size: 12.5px; line-height: 20px; color: var(--ink-body); }
  .feature svg { position: absolute; left: 0; top: -2px; }

  .references {
    left: 91px; top: 830px; width: 978px; height: 170px; box-sizing: border-box;
    background: var(--refs-bg); border-left: 1px solid var(--line); border-right: 1px solid var(--line);
  }
  .references h2 { position: absolute; left: 18px; top: 20px; margin: 0; font-size: 18.5px; font-weight: 600; color: #555; }
  .ref-thumb {
    position: absolute; top: 68px; width: 190px; height: 110px;
    background: linear-gradient(#3f9ad6, #8ac4ea 60%, #cfe6f5); box-shadow: 0 0 3px rgba(0,0,0,0.3);
  }
  .ref-zoom {
    position: absolute; top: 58px; width: 32px; height: 32px; border-radius: 50%;
    background: radial-gradient(#f4f4f4, #cfd2d5); box-shadow: 0 1px 3px rgba(0,0,0,0.35);
    display: flex; align-items: center; justify-content: center;
  }
</style>
</head>
<body>
<div class="stage">
  <div class="abs top-band"></div>

  <header>
    <div class="abs brand">
      <span class="brand-dot"></span>
      <span class="brand-name">BoltNet</span>
    </div>
    <div class="abs language">
      <span>CHOOSE LANGUAGE:</span>
      <svg width="18" height="12" viewBox="0 0 18 12" role="img" aria-label="English">
        <rect width="18" height="12" fill="#c8383d"/>
        <rect y="2" width="18" height="2" fill="#fff"/><rect y="6" width="18" height="2" fill="#fff"/><rect y="10" width="18" height="2" fill="#fff"/>
        <rect width="8" height="6" fill="#3a4f8f"/>
      </svg>
      <svg width="18" height="12" viewBox="0 0 18 12" role="img" aria-label="Nederlands">
        <rect width="18" height="4" fill="#c33a3f"/><rect y="4" width="18" height="4" fill="#fff"/><rect y="8" width="18" height="4" fill="#2d4f95"/>
      </svg>
    </div>
  </header>

  <nav class="abs main-nav">
    <a class="active" href="#" style="width:85px">Home</a>
    <a href="#" style="width:100px">Services</a>
    <a href="#" style="width:120px">References</a>
    <a href="#" style="width:90px">News</a>
    <a href="#" style="width:130px">About BoltNet</a>
    <a href="#" style="width:100px">Contact</a>
    <form class="abs search">
      <input type="text" placeholder="E.g Cool Application">
      <button type="button">FIND</button>
    </form>
  </nav>

  <section class="abs hero">
    <div class="abs hero-photo" role="img" aria-label="Business person touching a glowing network of connected contacts"></div>
    <h1 class="abs hero-title">We Creat Great &amp; Easy-to-Use Applications !</h1>
    <p class="abs hero-copy">Lorem ipsum dolor sit amet, consectetur adipisicing elit, sed do eiusmod tempor incididunt ut labore et dolore magna aliqua. Ut enim ad minim veniam, quis nostrud exercitation ullamco laboris nisi ut aliquip ex ea commodo consequat.Lorem ipsum dolor sit amet, consectetur adipisic-ing elit, sed do eiusmod tempor incididunt ut labore et dolore magna aliqua. Ut enim ad minim veniam, quis nostrud exercitation ullamco laboris nisi ut aliquip ex ea commodo consequat.</p>
    <a class="abs hero-cta">Learn More</a>
  </section>
  <div class="abs slider-arrow" style="left:81px">
    <svg width="34" height="24" viewBox="0 0 34 24"><polygon points="2,12 14,2 14,8 32,8 32,16 14,16 14,22" fill="#dfe8f1" stroke="#7f97af"/></svg>
  </div>
  <div class="abs slider-arrow" style="left:1021px">
    <svg width="34" height="24" viewBox="0 0 34 24"><polygon points="32,12 20,2 20,8 2,8 2,16 20,16 20,22" fill="#dfe8f1" stroke="#7f97af"/></svg>
  </div>

  <section class="abs news-strip">
    <article class="news-item" style="width:322px">
      <h3>Very Long News Title Here</h3>
      <p>Lorem ipsum dolor sit amet, consectetur adipisicing elit, sed do eiusmod tempor incididunt ut labore et.</p>
      <a href="#">Read more</a>
    </article>
    <article class="news-item" style="width:333px;padding-left:29px">
      <h3>Very Long News Title Here</h3>
      <p>Lorem ipsum dolor sit amet, consectetur adipisicing elit, sed do eiusmod tempor incididunt ut labore et.</p>
      <a href="#">Read more</a>
    </article>
    <article class="news-item" style="width:323px;padding-left:26px;padding-top:15px">
      <h3>Very Long News Title Here</h3>
      <p>Lorem ipsum dolor sit amet, consectetur adipisicing elit, sed do eiusmod tempor incididunt ut labore et.</p>
      <a href="#">Read more</a>
    </article>
  </section>

  <div class="abs why-bar">
    <h2>Why Choose BoltNet ?</h2>
    <a class="why-button">Our Services</a>
  </div>

  <section class="abs features">
    <div class="feature" style="left:19px;top:24px">
      <svg width="30" height="32" viewBox="0 0 30 32">
        <rect x="2" y="3" width="26" height="28" rx="2" fill="#f3e3c6" stroke="#b3651f" stroke-width="2"/>
        <rect x="9" y="0.5" width="12" height="5" rx="1" fill="#8a8f95"/>
        <path d="M7 12l2 2 3-4M7 19l2 2 3-4M7 26l2 2 3-4" stroke="#555" stroke-width="1.4" fill="none"/>
        <path d="M15 12h9M15 19h9M15 26h9" stroke="#777" stroke-width="1.4"/>
      </svg>
      <h3>Problem Solver</h3>
      <p>Lorem ipsum dolor sit amet, consectetur adipisicing elit, sed do eiusmod tempor incidid-unt ut labore et dolore magna aliqua. Ut enim ad minim veniam, quis nostrud exercitation ullamco laboris nisi ut aliquip ex ea commodo.</p>
    </div>
    <div class="feature" style="left:335px;top:20px">
      <svg width="32" height="26" viewBox="0 0 32 26">
        <rect x="1" y="1" width="30" height="24" rx="1" fill="#2b2d30" stroke="#777"/>
        <path d="M5 7l3 2-3 2M10 11h5" stroke="#9ad" stroke-width="1.2" fill="none"/>
      </svg>
      <h3>Innovation and reliability</h3>
      <p>Lorem ipsum dolor sit amet, consectetur adipisicing elit, sed do eiusmod tempor incidid-unt ut labore et dolore magna aliqua. Ut enim ad minim veniam, quis nostrud exercitation ullamco laboris nisi ut aliquip ex ea commodo.</p>
    </div>
    <div class="feature" style="left:670px;top:20px">
      <svg width="34" height="28" viewBox="0 0 34 28">
        <path d="M17 2C8 2 2 7 2 13c0 3 2 6 5 8l-2 6 7-4c2 .5 3 .5 5 .5 9 0 15-5 15-10.5S26 2 17 2z" fill="#fafafa" stroke="#9aa0a6" stroke-width="1.4"/>
      </svg>
      <h3>Popular community</h3>
      <p>Lorem ipsum dolor sit amet, consectetur adipisicing elit, sed do eiusmod tempor incidid-unt ut labore et dolore magna aliqua. Ut enim ad minim veniam, quis nostrud exercitation ullamco laboris nisi ut aliquip ex ea commodo.</p>
    </div>
  </section>

  <section class="abs references">
    <h2>Look Our References</h2>
    <div class="ref-thumb" style="left:23px" role="img" aria-label="Screenshot of a reference website"></div>
    <div class="ref-zoom" style="left:188px"><svg width="14" height="14" viewBox="0 0 14 14"><path d="M7 1v12M1 7h12" stroke="#555" stroke-width="3"/></svg></div>
    <div class="ref-thumb" style="left:268px" role="img" aria-label="Screenshot of a reference website"></div>
    <div class="ref-zoom" style="left:433px"><svg width="14" height="14" viewBox="0 0 14 14"><path d="M7 1v12M1 7h12" stroke="#555" stroke-width="3"/></svg></div>
    <div class="ref-thumb" style="left:513px" role="img" aria-label="Screenshot of a reference website"></div>
    <div class="ref-zoom" style="left:678px"><svg width="14" height="14" viewBox="0 0 14 14"><path d="M7 1v12M1 7h12" stroke="#555" stroke-width="3"/></svg></div>
    <div class="ref-thumb" style="left:758px" role="img" aria-label="Screenshot of a reference website"></div>
    <div class="ref-zoom" style="left:923px"><svg width="14" height="14" viewBox="0 0 14 14"><path d="M7 1v12M1 7h12" stroke="#555" stroke-width="3"/></svg></div>
  </section>
</div>
</body>
</html>
```